Business Card design for a company called Tully Brook Co

I need a business card design for my oil fired boiler servicing company. I have a logo design already and Im just looking that incorporated into the business card design. card details; Tully Brook Co
Oil Burner Servicing - Mid Ulster Area
Service Engineer - Owen Madler
Mobile 07700914862
email - Tully.Brook.Co@quillpost.net
www.tullybrookco.net
I carry out Servicing, Commissioning, Fault Finding, Warranty Validation
Target Market(s)
home owners with oil fired central heating
Industry/Entity Type
Business
Contact Information for Business Card
Tully Brook Co
Tell. 07700914862
Web: www.tullybrookco.net
email Tully.Brook.Co@Quillpost.Net
Servicing Fault Finding Commissioning Warranty Validation
Look and feel

```html
<!DOCTYPE html>
<html lang="en">
<head>
<meta charset="utf-8">
<title>Tully Brook Co – Business Card</title>
<link href="https://fonts.googleapis.com/css2?family=Rubik:wght@500&family=Roboto:ital,wght@0,400;0,500;0,700;1,400&display=swap" rel="stylesheet">
<style>
  :root {
    --backdrop: #cbcbcb;
    --card-dark: #000000;
    --card-light: #f7f7f7;
    --brand-green: #2eaa3c;
    --band-top: #5fc23a;
    --band-bottom: #0ea33f;
    --text-dark: #333333;
    --white: #ffffff;
    --ghost-dark: #1b1b1b;
    --ghost-light: #dcefe1;
  }
  html, body {
    margin: 0;
    width: 1200px;
    height: 1004px;
    overflow: hidden;
    background: var(--backdrop);
  }
  .canvas { position: relative; width: 1200px; height: 1004px; }
  .card {
    position: absolute;
    left: 316px;
    width: 568px;
    height: 342px;
    overflow: hidden;
    box-shadow: 4px 5px 8px rgba(0,0,0,0.3);
  }
  .card-front { top: 148px; background: var(--card-dark); }
  .card-back { top: 513px; background: var(--card-light); }

  .ghost-ring { position: absolute; border-radius: 50%; box-sizing: border-box; }
  .card-front .ghost-ring {
    left: 325px; top: 32px; width: 232px; height: 232px;
    border: 18px solid var(--ghost-dark);
  }
  .card-back .ghost-ring {
    left: 374px; top: 152px; width: 176px; height: 176px;
    border: 14px solid var(--ghost-light);
  }

  .brand-dot {
    position: absolute; width: 88px; height: 88px; border-radius: 50%;
    background: var(--brand-green);
  }
  .card-front .brand-dot { left: 77px; top: 108px; }
  .card-back .brand-dot { left: 81px; top: 47px; }

  .brand-name {
    position: absolute; margin: 0;
    font-family: "Rubik", sans-serif; font-weight: 500;
    font-size: 40px; line-height: 1;
    color: var(--brand-green); white-space: nowrap;
  }
  .brand-tagline {
    position: absolute; margin: 0;
    font-family: "Rubik", sans-serif; font-weight: 500;
    font-size: 10.5px; letter-spacing: 1.6px;
    color: var(--brand-green); white-space: nowrap;
  }
  .card-front .brand-name { left: 186px; top: 123px; }
  .card-front .brand-tagline { left: 187px; top: 171px; }
  .card-back .brand-name { left: 178px; top: 66px; }
  .card-back .brand-tagline { left: 179px; top: 108px; }

  .service-band {
    position: absolute; left: 0; bottom: 0; width: 100%; height: 40px;
    background: linear-gradient(var(--band-top), var(--band-bottom));
    display: flex; align-items: center; justify-content: center;
    font-family: "Roboto", sans-serif; font-size: 14px; color: var(--white);
    white-space: pre;
  }

  .side-strip {
    position: absolute; left: 0; top: 0; width: 49px; height: 100%;
    background: linear-gradient(var(--band-top), var(--band-bottom));
  }
  .side-rule {
    position: absolute; left: 49px; top: 0; width: 5px; height: 100%;
    background: var(--card-dark);
  }

  .person-name {
    position: absolute; left: 86px; top: 184px; margin: 0;
    font-family: "Roboto", sans-serif; font-weight: 500; font-size: 22px;
    color: var(--brand-green);
  }
  .person-role {
    position: absolute; left: 86px; top: 215px; margin: 0;
    font-family: "Roboto", sans-serif; font-style: italic; font-size: 12.5px;
    color: var(--text-dark);
  }
  .contact-list {
    position: absolute; left: 86px; top: 248px; margin: 0; padding: 0;
    list-style: none; font-family: "Roboto", sans-serif; font-size: 15px;
    color: var(--text-dark);
  }
  .contact-list li { display: flex; align-items: center; height: 22.5px; }
  .contact-list svg { width: 14px; height: 14px; margin-right: 14px; fill: var(--brand-green); }
</style>
</head>
<body>
<div class="canvas">

  <section class="card card-front">
    <div class="ghost-ring"></div>
    <div class="brand-dot"></div>
    <h1 class="brand-name">Tully Brook Co</h1>
    <p class="brand-tagline">OIL BURNER SERVICING - MID ULSTER AREA</p>
    <div class="service-band">Servicing  |  Commissioning  |  Fault Finding  |  Warranty Validation</div>
  </section>

  <section class="card card-back">
    <div class="side-strip"></div>
    <div class="side-rule"></div>
    <div class="ghost-ring"></div>
    <div class="brand-dot"></div>
    <h2 class="brand-name">Tully Brook Co</h2>
    <p class="brand-tagline">OIL BURNER SERVICING - MID ULSTER AREA</p>
    <h3 class="person-name">Owen Madler</h3>
    <p class="person-role">Service Engineer</p>
    <ul class="contact-list">
      <li>
        <svg viewBox="0 0 16 16" aria-hidden="true"><path d="M1 5c0-2 3-3 7-3s7 1 7 3v1h-4V5H5v1H1zM4 7h8l2 6H2z"/></svg>
        07700914862
      </li>
      <li>
        <svg viewBox="0 0 16 16" aria-hidden="true"><path d="M8 1a7 7 0 1 0 0 14A7 7 0 0 0 8 1zm0 1.5c.8 0 1.7 1.5 2 4H6c.3-2.5 1.2-4 2-4zM2.6 6.5h2c-.1.5-.1 1-.1 1.5s0 1 .1 1.5h-2a5.5 5.5 0 0 1 0-3zm3.4 3h4c-.3 2.5-1.2 4-2 4s-1.7-1.5-2-4zm5.4 0c.1-.5.1-1 .1-1.5s0-1-.1-1.5h2a5.5 5.5 0 0 1 0 3z"/></svg>
        www.tullybrookco.net
      </li>
      <li>
        <svg viewBox="0 0 16 16" aria-hidden="true"><path d="M1 3h14v10H1zm1.5 1.5v.3L8 9l5.5-4.2v-.3zm0 2.2v4.8h11V6.7L8 11z"/></svg>
        Tully.Brook.Co@Quillpost.Net
      </li>
    </ul>
  </section>

</div>
</body>
</html>
```